Bluefinch Painting needs a Website

We need a website built for a Painting company I own, we mainly do residential painting, but don't want to be limited to that.

Need to have estimate request form.
Need pic's of past projects

I like the look of the website for http://www.harborline-painters.example
& "Thistledown Property inspections"

My logo that was designed here on ArtHive on the front page

I would like one of the houses I downloaded as part of the background
of the front page.

Target Market(s)

Home owners

Industry/Entity Type

Painting

Number of Pages Required

1 page

Font styles to use
Serif

Requirements
Must have
• Estimate request form for home owners to fill out -
• Name:
• Phone Number:
• Address:
• E-mail:
• Painting project description:
• And my info to:
• My phone number: (555) 318-7764
• My web address bluefinchpainting.example
Nice to have
• My logo that was designed here on ArtHive

```html
<!DOCTYPE html>
<html lang="en">
<head>
<meta charset="utf-8">
<title>Bluefinch Painting</title>
<link rel="stylesheet" href="https://fonts.googleapis.com/css2?family=Roboto+Slab:wght@300;400&display=swap">
<style>
:root{
  --blue:#2174bf;
  --blue-dark:#1b5e9f;
  --sky:#3dbbe9;
  --ink:#333;
  --muted:#666;
  --paper:#fff;
  --mist:#f1f4f7;
  --footer:#1e1e1e;
  --footer-deep:#121212;
  --footer-text:#dddddd;
  --line:#9bb8d6;
}
*{box-sizing:border-box;margin:0;padding:0}
html,body{width:1080px;height:1200px;overflow:hidden;background:var(--paper)}
body{font-family:"Roboto Slab",Georgia,serif;color:var(--ink)}
.stage{position:absolute;left:0;top:0;width:1350px;height:1500px;transform:scale(.8);transform-origin:0 0}
.site{position:absolute;left:250px;top:0;width:850px;height:1497px;overflow:hidden}
.abs{position:absolute}

/* top bar */
.topbar{left:0;top:0;width:850px;height:32px;background:var(--blue);color:#fff;font-size:12px}
.topbar .phone{left:58px;top:8px;display:flex;align-items:center;gap:14px;white-space:nowrap}
.topbar .social{right:56px;top:6px;display:flex;gap:9px}
.topbar .social span{width:19px;height:19px;border-radius:50%;display:block}
.topbar .social span:nth-child(1){background:#1c4f9c}
.topbar .social span:nth-child(2){background:#3db5ea}
.topbar .social span:nth-child(3){background:#d93a24}
.topbar .social span:nth-child(4){background:#2aa3d8}

/* header */
.header{left:0;top:32px;width:850px;height:62px;background:#fff}
.brand{left:57px;top:18px;display:flex;align-items:center;gap:8px;font-size:19px;color:var(--ink);letter-spacing:.5px;white-space:nowrap}
.brand .mark{width:22px;height:22px;background:var(--sky);display:block}
.nav{left:346px;top:22px;display:flex;font-size:11px;color:var(--ink);white-space:nowrap}
.nav a{color:inherit;text-decoration:none;padding:3px 13px;line-height:12px;margin-right:2px}
.nav a.active{background:var(--sky);color:#fff}

/* hero */
.hero{left:0;top:94px;width:850px;height:356px;background:linear-gradient(180deg,#6aa9e0 0%,#b9cad6 28%,#a3947f 55%,#5c7a3e 78%,#3d6a33 100%)}
.hero-band{left:0;top:378px;width:850px;height:72px;background:rgba(39,112,178,.88)}
.hero-badge{left:391px;top:338px;width:68px;height:68px;border-radius:50%;background:var(--sky);border:3px solid #fff}
.hero-title{left:0;top:416px;width:850px;text-align:center;color:#fff;font-size:20px;font-weight:300;letter-spacing:.2px;white-space:nowrap}

/* why */
.why{left:0;top:450px;width:850px;height:267px;background:var(--mist)}
.why h2{left:57px;top:28px;font-size:17px;font-weight:300;color:var(--blue);white-space:nowrap}
.why p{left:57px;top:58px;width:418px;font-size:9px;line-height:15px;color:var(--muted)}
.feature{top:164px;width:90px;text-align:center;font-size:12px}
.feature .icon{width:48px;height:48px;margin:0 auto 9px;border:2px solid var(--blue);border-radius:50%;background:#fff;display:flex;align-items:center;justify-content:center}
.video{left:498px;top:32px;width:296px;height:204px;background:linear-gradient(160deg,#7c8fa6,#d7dde4 45%,#8a9199)}
.video .play{left:124px;top:66px;width:46px;height:46px;border-radius:50%;background:#fff;display:flex;align-items:center;justify-content:center}
.video .bar{left:0;bottom:0;width:296px;height:28px;background:rgba(15,30,50,.85);color:#fff;font-size:9px}

/* projects */
.projects{left:0;top:717px;width:850px;height:264px;background:linear-gradient(90deg,#1f4f91,#3f87d1 30%,#2e6fbd 50%,#3f87d1 70%,#1f4f91)}
.projects h2{left:0;top:26px;width:850px;text-align:center;color:#fff;font-size:21px;font-weight:300}
.card{top:83px;width:130px;height:142px}
.card .back{left:4px;top:-4px;width:130px;height:142px;background:#f3f3f3;transform:rotate(3deg)}
.card .front{left:0;top:0;width:130px;height:142px;background:#fff;box-shadow:0 2px 6px rgba(0,0,0,.3)}
.card .photo{left:6px;top:6px;width:118px;height:99px}
.card .zoom{right:6px;top:83px;width:22px;height:22px;background:var(--blue);display:flex;align-items:center;justify-content:center}
.card .label{left:0;top:112px;width:130px;text-align:center;font-size:11px}

/* quote */
.quote{left:0;top:981px;width:850px;height:315px;background:linear-gradient(180deg,#f4f6f8,#e9edf1 60%,#f1f3f5)}
.quote h2{left:0;top:26px;width:850px;text-align:center;color:var(--blue);font-size:21px;font-weight:300}
.field{width:233px}
.field label{display:block;font-size:11px;font-weight:300;color:var(--sky);margin-bottom:4px;white-space:nowrap}
.field .input{height:26px;border:1px solid var(--line);background:rgba(255,255,255,.6)}
.field .area{height:85px}
.send{left:308px;top:258px;width:233px;height:26px;background:var(--sky);color:#fff;font-size:16px;font-weight:300;text-align:center;line-height:26px}

/* footer */
.footer{left:0;top:1296px;width:850px;height:174px;background:var(--footer);color:var(--footer-text);font-size:9.5px}
.col h3{font-size:10px;font-weight:400;color:var(--sky);padding-bottom:4px;border-bottom:1px solid #555;margin-bottom:4px;white-space:nowrap}
.col ul{list-style:none}
.col li{line-height:16px;border-bottom:1px solid #3a3a3a;color:var(--footer-text);white-space:nowrap}
.col .plain{line-height:13.5px;white-space:nowrap}
.col .plain a{color:var(--sky);text-decoration:none}
.trailer{left:588px;top:14px;width:206px;height:145px;background:linear-gradient(180deg,#eef1f3,#c8cdd2 75%,#2a2a2a)}
.copyright{left:0;top:1470px;width:850px;height:27px;background:var(--footer-deep);color:#888;font-size:8px;text-align:center;line-height:27px}
</style>
</head>
<body>
<div class="stage">
<div class="site">

  <div class="abs topbar">
    <div class="abs phone">
      <svg width="14" height="14" viewBox="0 0 24 24"><path fill="#fff" d="M6.6 10.8a15 15 0 0 0 6.6 6.6l2.2-2.2a1 1 0 0 1 1-.25 11 11 0 0 0 3.6.6 1 1 0 0 1 1 1V20a1 1 0 0 1-1 1A17 17 0 0 1 3 4a1 1 0 0 1 1-1h3.5a1 1 0 0 1 1 1 11 11 0 0 0 .6 3.6 1 1 0 0 1-.25 1z"/></svg>
      <span>(555) 318-7764</span>
    </div>
    <div class="abs social"><span></span><span></span><span></span><span></span></div>
  </div>

  <div class="abs header">
    <div class="abs brand"><span class="mark"></span><span>BLUEFINCH PAINTING</span></div>
    <nav class="abs nav">
      <a class="active">HOME</a><a>ABOUT</a><a>SERVICES</a><a>PROJECTS</a><a>TESTIMONIALS</a><a>FREE QUOTE</a>
    </nav>
  </div>

  <div class="abs hero" role="img" aria-label="Two-storey house with fresh paint behind flowering shrubs"></div>
  <div class="abs hero-band"></div>
  <div class="abs hero-badge"></div>
  <div class="abs hero-title">A WORLD OF NEW COLOR THAT WILL TRANSFORM YOUR WORLD.</div>

  <section class="abs why">
    <h2 class="abs">WHY BLUEFINCH PAINTING</h2>
    <p class="abs">Lorem Ipsum is simply dummy text of the printing and typesetting industry. Lorem Ipsum has been the industry's standard dummy text ever since the 1500s, when an unknown printer took a galley of type and scrambled it to make a type specimen book. It has survived not only five centuries, but also the leap into electronic typesetting, remaining essentially unchanged. It was popularised in the 1960s with the release of Lettrafix sheets containing Lorem Ipsum passages, and more recently with desktop publishing software like Pagecraft Studio including versions of Lorem Ipsum.</p>
    <div class="abs feature" style="left:41px">
      <div class="icon"><svg width="24" height="24" viewBox="0 0 24 24"><rect x="3" y="12" width="4" height="9" fill="#2174bf"/><rect x="10" y="8" width="4" height="13" fill="#2174bf"/><rect x="17" y="4" width="4" height="17" fill="#2174bf"/></svg></div>Experience</div>
    <div class="abs feature" style="left:193px">
      <div class="icon"><svg width="24" height="24" viewBox="0 0 24 24"><circle cx="12" cy="9" r="6" fill="#2174bf"/><path d="M8 14l-2 8 6-3 6 3-2-8z" fill="#2174bf"/><circle cx="12" cy="9" r="3" fill="#fff"/></svg></div>Quality</div>
    <div class="abs feature" style="left:345px">
      <div class="icon"><svg width="24" height="24" viewBox="0 0 24 24"><path d="M14 3l7 7-5 5-7-7z" fill="#2174bf"/><path d="M10 12l-7 7 2 2 7-7z" fill="#2174bf"/></svg></div>Service</div>
    <div class="abs video" role="img" aria-label="Video of the company trailer parked outside">
      <div class="abs play"><svg width="14" height="16" viewBox="0 0 14 16"><path d="M2 1l11 7-11 7z" fill="#222"/></svg></div>
      <div class="abs bar">
        <svg class="abs" style="left:10px;top:9px" width="10" height="10" viewBox="0 0 10 10"><path d="M1 0l8 5-8 5z" fill="#3dbbe9"/></svg>
        <div class="abs" style="left:32px;top:13px;width:218px;height:2px;background:#fff"></div>
        <div class="abs" style="left:32px;top:13px;width:108px;height:2px;background:#3dbbe9"></div>
        <div class="abs" style="left:137px;top:10px;width:7px;height:7px;border-radius:50%;background:#fff"></div>
        <span class="abs" style="left:262px;top:9px">12.30</span>
      </div>
    </div>
  </section>

  <section class="abs projects" role="img" aria-label="Blue-toned background of a painter framing a view with hands">
    <h2 class="abs">PROJECTS</h2>
    <div class="abs card" style="left:66px"><div class="abs back"></div><div class="abs front">
      <div class="abs photo" role="img" aria-label="Painted entryway with pink flowers" style="background:linear-gradient(180deg,#7a7468,#5d6550 60%,#b24b6a)"></div>
      <div class="abs zoom"><svg width="14" height="14" viewBox="0 0 14 14"><circle cx="6" cy="6" r="4" fill="none" stroke="#fff" stroke-width="2"/><path d="M9 9l4 4" stroke="#fff" stroke-width="2"/></svg></div>
      <div class="abs label">Project 1</div></div></div>
    <div class="abs card" style="left:262px"><div class="abs back"></div><div class="abs front">
      <div class="abs photo" role="img" aria-label="Street of painted homes with trees" style="background:linear-gradient(180deg,#c9d6de,#4f6a44 50%,#7d7c7a)"></div>
      <div class="abs zoom"><svg width="14" height="14" viewBox="0 0 14 14"><circle cx="6" cy="6" r="4" fill="none" stroke="#fff" stroke-width="2"/><path d="M9 9l4 4" stroke="#fff" stroke-width="2"/></svg></div>
      <div class="abs label">Project 2</div></div></div>
    <div class="abs card" style="left:459px"><div class="abs back"></div><div class="abs front">
      <div class="abs photo" role="img" aria-label="Painted house front with lawn" style="background:linear-gradient(180deg,#8fbbe4,#8f8573 45%,#4f7a38)"></div>
      <div class="abs zoom"><svg width="14" height="14" viewBox="0 0 14 14"><circle cx="6" cy="6" r="4" fill="none" stroke="#fff" stroke-width="2"/><path d="M9 9l4 4" stroke="#fff" stroke-width="2"/></svg></div>
      <div class="abs label">Project 3</div></div></div>
    <div class="abs card" style="left:655px"><div class="abs back"></div><div class="abs front">
      <div class="abs photo" role="img" aria-label="Painted house with patio" style="background:linear-gradient(180deg,#9aa2a8,#6d6a64 55%,#555)"></div>
      <div class="abs zoom"><svg width="14" height="14" viewBox="0 0 14 14"><circle cx="6" cy="6" r="4" fill="none" stroke="#fff" stroke-width="2"/><path d="M9 9l4 4" stroke="#fff" stroke-width="2"/></svg></div>
      <div class="abs label">Project 4</div></div></div>
  </section>

  <section class="abs quote" role="img" aria-label="Faint background of a house window">
    <h2 class="abs">FREE QUOTE</h2>
    <div class="abs field" style="left:157px;top:79px"><label>NAME:</label><div class="input"></div></div>
    <div class="abs field" style="left:460px;top:79px"><label>EMAIL:</label><div class="input"></div></div>
    <div class="abs field" style="left:157px;top:138px"><label>PHONE NUMBER:</label><div class="input"></div></div>
    <div class="abs field" style="left:460px;top:138px"><label>MESSAGE:</label><div class="input area"></div></div>
    <div class="abs field" style="left:157px;top:197px"><label>ADDRESS:</label><div class="input"></div></div>
    <div class="abs send">SEND</div>
  </section>

  <footer class="abs footer">
    <div class="abs col" style="left:56px;top:30px;width:116px">
      <h3>QUICK LINKS</h3>
      <ul><li>Home</li><li>About</li><li>Services</li><li>Projects</li><li>Testimonials</li><li style="border:none">Free Quote</li></ul>
    </div>
    <div class="abs col" style="left:207px;top:30px;width:158px">
      <h3>SERVICES</h3>
      <ul style="width:115px"><li>View all services</li><li style="border:none">View and book us</li></ul>
    </div>
    <div class="abs col" style="left:404px;top:30px;width:156px">
      <h3>ADDRESS</h3>
      <div class="plain">Lorem gate 24, 5548 Harbor<br>Tel: (555) 318-7764<br>Email: <a>post@bluefinchpainting.example</a></div>
    </div>
    <div class="abs trailer" role="img" aria-label="White company trailer with blue lettering"></div>
  </footer>
  <div class="abs copyright">Copyright bluefinchpainting.example. All rights reserved.</div>

</div>
</div>
</body>
</html>
```